Business Stationery Design

I would like to get some stationery designed for my company. The stationery should include a letterhead, envelope, and business card. We are a technology consulting company specializing in Healthcare IT, and Education management systems. The colors of the stationery should match the logo. The logo is uploaded.

Target Market(s)

Hospitals, Clinics. Doctors offices. Private Schools.

Industry/Entity Type

Business

```html
<!DOCTYPE html>
<html lang="en">
<head>
<meta charset="utf-8">
<title>Clearbrook Consulting Group – Stationery</title>
<link href="https://fonts.googleapis.com/css2?family=Montserrat:wght@400;600;700&family=Open+Sans:wght@400;600&display=swap" rel="stylesheet">
<style>
  :root{
    --green:#7dc13a;
    --green-soft:#95cd5c;
    --yellow:#f7b500;
    --paper:#ffffff;
    --backdrop:#e9eaea;
    --ink:#3d3d3d;
    --ink-soft:#6b6b6b;
  }
  *{box-sizing:border-box;margin:0;padding:0}
  html,body{width:1200px;height:605px;overflow:hidden;background:var(--backdrop)}
  body{position:relative;font-family:"Open Sans",Arial,sans-serif;color:var(--ink)}
  .sheet{position:absolute;background:var(--paper);box-shadow:0 1px 3px rgba(0,0,0,.18);overflow:hidden}

  /* brand name lock-up */
  .brand{display:flex;align-items:center;gap:4px;font-family:"Open Sans",Arial,sans-serif;font-weight:600;color:var(--green);white-space:nowrap}
  .brand-dot{border-radius:50%;background:var(--green);flex:none}
  .brand.on-green{color:#fff}
  .brand.on-green .brand-dot{background:#fff}

  .contact{font-family:"Montserrat",Arial,sans-serif;font-weight:600;color:#fff;line-height:1.3}
  .contact-row{display:flex;align-items:center;gap:4px}
  .contact-row svg{flex:none}

  .foliage{position:absolute;background:radial-gradient(ellipse at 40% 60%,rgba(255,255,255,.22),rgba(255,255,255,0) 70%)}

  /* business card front */
  .card-front{left:58px;top:47px;width:154px;height:86px}
  .card-front .person{position:absolute;left:12px;top:17px;font-family:"Montserrat",Arial,sans-serif}
  .card-front .person-name{font-size:7px;font-weight:700;color:var(--green)}
  .card-front .person-role{font-size:4.6px;color:var(--ink-soft);margin-top:2px}
  .card-front .brand{position:absolute;left:110px;top:21px;font-size:6px}
  .card-front .stripe{position:absolute;left:0;right:0;top:56px;height:3px;background:var(--yellow)}
  .card-front .band{position:absolute;left:0;right:0;top:59px;bottom:0;background:var(--green)}
  .card-front .contact{position:absolute;font-size:4.2px;top:9px}

  /* business card back */
  .card-back{left:243px;top:47px;width:153px;height:86px}
  .card-back .brand{position:absolute;left:50%;top:30px;transform:translateX(-50%);font-size:8px}
  .card-back .web{position:absolute;left:0;right:0;top:70px;text-align:center;font-family:"Montserrat",Arial,sans-serif;font-size:4.3px;font-weight:600;color:var(--green)}

  /* envelope back */
  .envelope-back{left:24px;top:157px;width:372px;height:189px}
  .envelope-back .brand{position:absolute;left:50%;top:148px;transform:translateX(-50%);font-size:11px}

  /* envelope front */
  .envelope-front{left:24px;top:371px;width:372px;height:190px;background:var(--green)}
  .envelope-front .addressee{position:absolute;left:278px;top:102px;font-family:"Montserrat",Arial,sans-serif;color:#fff}
  .envelope-front .addressee-name{font-size:7.5px;font-weight:600}
  .envelope-front .addressee-role{font-size:5px;margin-top:2px}
  .envelope-front .contact{position:absolute;left:278px;top:124px;font-size:5px}
  .envelope-front .contact-row{margin-bottom:5px}
  .envelope-front .web-bar{position:absolute;left:278px;top:168px;width:88px;height:9px;background:var(--yellow);color:#fff;font-family:"Montserrat",Arial,sans-serif;font-weight:600;font-size:4.8px;padding:2px 0 0 4px}

  /* letterhead */
  .letterhead{left:423px;top:47px;width:365px;height:513px}
  .letterhead .sidebar{position:absolute;left:23px;top:26px;width:86px;height:458px;background:var(--green);border-radius:2px 2px 0 0}
  .letterhead .sidebar .contact{position:absolute;left:8px;top:402px;font-size:5px}
  .letterhead .sidebar .contact-row{margin-top:4px}
  .letterhead .sidebar-web{position:absolute;left:23px;top:472px;width:86px;height:12px;background:var(--yellow);color:#fff;font-family:"Montserrat",Arial,sans-serif;font-weight:600;font-size:5.3px;padding:3px 0 0 8px}
  .letterhead .brand{position:absolute;left:255px;top:86px;font-size:11px}
  .letter{position:absolute;left:129px;top:176px;width:212px}
  .letter-greeting{font-size:9px;margin-bottom:10px}
  .letter p{font-size:5.9px;line-height:9.3px;text-align:justify;color:var(--ink);margin-bottom:9px}
  .letter-sign{position:absolute;left:129px;top:479px;font-size:5.9px;line-height:9.3px}

  /* folder */
  .folder{left:811px;top:47px;width:366px;height:513px;background:var(--green)}
  .folder .brand{position:absolute;left:50%;top:140px;transform:translateX(-50%);font-size:13px}
</style>
</head>
<body>

  <!-- business card front -->
  <section class="sheet card-front">
    <div class="person">
      <div class="person-name">Name Surname</div>
      <div class="person-role">POSITION</div>
    </div>
    <div class="brand"><span class="brand-dot" style="width:6px;height:6px"></span></div>
    <div class="stripe"></div>
    <div class="band">
      <div class="contact" style="left:12px">0000 Main Street, Ste. 000<br>City name, NY 00000</div>
      <div class="contact" style="left:86px">
        <div class="contact-row"><svg width="4" height="4" viewBox="0 0 10 10"><circle cx="5" cy="5" r="5" fill="#fff"/></svg>000-110-2200</div>
        <div class="contact-row"><svg width="4" height="4" viewBox="0 0 10 10"><rect y="2" width="10" height="6" fill="#fff"/></svg>office@clearbrookcg.com</div>
      </div>
    </div>
  </section>

  <!-- business card back -->
  <section class="sheet card-back">
    <div class="brand"><span class="brand-dot" style="width:6px;height:6px"></span>Clearbrook</div>
    <div class="web">www.clearbrookcg.com</div>
  </section>

  <!-- envelope back -->
  <section class="sheet envelope-back">
    <svg width="372" height="60" viewBox="0 0 372 60" style="position:absolute;left:0;top:0">
      <path d="M0 0H372V22Q372 34 350 36L186 56L22 36Q0 34 0 22Z" fill="var(--green)"/>
    </svg>
    <div class="brand"><span class="brand-dot" style="width:8px;height:8px"></span>Clearbrook</div>
  </section>

  <!-- envelope front -->
  <section class="sheet envelope-front">
    <div class="foliage" role="img" aria-label="Faint leaf pattern" style="left:10px;top:20px;width:250px;height:170px"></div>
    <div class="addressee">
      <div class="addressee-name">Name Surname</div>
      <div class="addressee-role">Position</div>
    </div>
    <div class="contact">
      <div class="contact-row" style="margin-bottom:8px">0000 Main Street, Ste. 000<br>City name, NY 00000</div>
      <div class="contact-row"><svg width="5" height="5" viewBox="0 0 10 10"><circle cx="5" cy="5" r="5" fill="#fff"/></svg>000-110-2200</div>
      <div class="contact-row"><svg width="5" height="5" viewBox="0 0 10 10"><rect y="2" width="10" height="6" fill="#fff"/></svg>office@clearbrookcg.com</div>
    </div>
    <div class="web-bar">www.clearbrookcg.com</div>
  </section>

  <!-- letterhead -->
  <section class="sheet letterhead">
    <div class="sidebar">
      <div class="foliage" role="img" aria-label="Faint leaf pattern" style="left:0;top:120px;width:86px;height:230px"></div>
      <div class="contact">
        <div>0000 Main Street, Ste. 000<br>City name, NY 00000</div>
        <div class="contact-row" style="margin-top:7px"><svg width="5" height="5" viewBox="0 0 10 10"><circle cx="5" cy="5" r="5" fill="#fff"/></svg>000-110-2200</div>
        <div class="contact-row"><svg width="5" height="5" viewBox="0 0 10 10"><rect y="2" width="10" height="6" fill="#fff"/></svg>office@clearbrookcg.com</div>
      </div>
    </div>
    <div class="sidebar-web">www.clearbrookcg.com</div>
    <div class="brand"><span class="brand-dot" style="width:8px;height:8px"></span>Clearbrook</div>

    <article class="letter">
      <div class="letter-greeting">Dear Client,</div>
      <p>Harum faccumquam quidel et, si deris am, sant.<br>Is repro et qui consequ atibusda nem ulpa velitius utatur, odi ut ut quoditi oratem quam exceria nobis et lit am, utem et laborer chillit, torestisit quundemporum aut magnis et latur sinvellanis quiaeperum quae lam etur sam escidestium diaecto estisque lam, am qui ipidigni-sin perum laborro optis repro et qui consequ atibusda nem ulpa velitius utatur, odi ut ut quoditi oratem quam ero iur, volupta dolorru mquatem rerum fugitatio. Nam lanis voluptatis suscipsa dolorehenis est quuntota sim intia porende ndant, to iur? Quis dem eum quatur solum qui int latur?<br>urio quam reste nullaborata animusam, omni necatet que plaudae porepudae sit alia pero iur, volupta dolorru mquatem rerum fugitatio. Nam lanis voluptatis suscipsa dolorehenis est quuntota sim intia porende ndant, to iur? Quis dem eum quatur solum qui int latur?</p>
      <p>Tem velupta volorehenim quiatio vendese quistio. Ullabor abore, ut ut volluptat odipsandust, consequ isquatione nia num res solum doluptas et, ne ped eumquia ndebitia nos repratquibus doluptatia quae odipsame voluptas et utatem que vid quibus ratem nos verferume nit et accus iust, con nim sitation rem aut la ea corest, qui consene stotat. Evenimilitem volesto officiliciis sequisc iducitaectus nihitis aut ipsae doluptas dus deligendi quatur?</p>
      <p>Pid ma sintoriamus aut et, nem expliquam eum ide volum in ellamus eum fugitatiam ipis init auteni officiis vent dolorio quodis andiorest veres dis quasper umquibust, ommolup turescimpe qui beriossecto.</p>
    </article>
    <div class="letter-sign">Sincerely,<br>Name Surname</div>
  </section>

  <!-- presentation folder -->
  <section class="sheet folder">
    <div class="brand on-green"><span class="brand-dot" style="width:10px;height:10px"></span>Clearbrook</div>
    <div class="foliage" role="img" aria-label="Faint leaf pattern" style="left:0;top:300px;width:320px;height:213px"></div>
  </section>

</body>
</html>
```